tourism marketplace web app redesign*

Hi, I need our front-page redesigned. For the competition please submit a jpg of ABOVE THE FOLD ONLY. The full page redesign will be a revision request. URL is https://qp.trolvexa.hu/hu/index.html login:'fullhd' and password:'asdasd' (Fold is supposed to be at "Kiemelt Ajanlatok", use all elements above that. Please use at least one extra color other than the two in the logo, or you may completely change them. FOCUS should be on the central combined search box (3 dropdown, 2 calendar picker + Kereses Button) just like nestorly.com, ravimoto.com, Pelusi.com, etc... The search box is always large, central, white, we want that too. We want it to look more modern, more clean AND we want to feature a changing beautiful nature photo background (like nestorly.com).Please use our newly designed logo (in attached pdf) and use that new spelling: "ferntrail.online"

```html
<!DOCTYPE html>
<html lang="en">
<head>
<meta charset="utf-8">
<title>ferntrail.online – Book your hunt directly</title>
<link href="https://fonts.googleapis.com/css2?family=Lato:wght@700;900&family=Open+Sans:wght@400;600;700&display=swap" rel="stylesheet">
<style>
  :root {
    --white: #ffffff;
    --ink: #222222;
    --ink-soft: #333333;
    --teal: #5aab97;
    --teal-dark: #4e9c89;
    --orange: #ff7f0a;
    --divider: #9a9a9a;
    --forest-1: #6f7470;
    --forest-2: #3d4540;
    --forest-3: #1f2a24;
    --bar-shade: rgba(40, 40, 40, 0.55);
  }
  * { box-sizing: border-box; margin: 0; padding: 0; }
  html, body {
    width: 1200px; height: 550px; overflow: hidden;
    background: var(--white);
    font-family: "Open Sans", Arial, sans-serif;
  }
  .page { position: relative; width: 1200px; height: 550px; overflow: hidden; }

  /* Header */
  .site-header {
    position: absolute; top: 0; left: 0; width: 1200px; height: 66px;
    background: var(--white); z-index: 2;
  }
  .brand {
    position: absolute; left: 87px; top: 12px; height: 42px;
    display: flex; align-items: center; gap: 9px; text-decoration: none;
  }
  .brand-mark { width: 42px; height: 42px; border-radius: 50%; background: var(--teal); }
  .brand-name {
    font-family: "Open Sans", Arial, sans-serif; font-weight: 600;
    font-size: 18px; color: var(--ink-soft);
  }
  .main-nav {
    position: absolute; right: 103px; top: 0; height: 66px;
    display: flex; align-items: center;
  }
  .main-nav a {
    font-size: 14px; color: var(--ink); text-decoration: none; margin-left: 22px;
  }
  .main-nav a:first-child { margin-left: 0; }
  .partner-button {
    margin-left: 26px !important;
    display: inline-flex; align-items: center; justify-content: center;
    width: 136px; height: 40px;
    border: 1px solid var(--teal); border-radius: 2px;
    color: var(--teal-dark) !important; font-weight: 700; font-size: 13px !important;
  }

  /* Hero */
  .hero {
    position: absolute; top: 66px; left: 0; width: 1200px; height: 484px;
  }
  .hero-photo {
    position: absolute; inset: 0;
    background:
      radial-gradient(ellipse 55% 45% at 50% 20%, rgba(150,155,150,0.55), transparent 70%),
      linear-gradient(180deg, var(--forest-1) 0%, var(--forest-2) 45%, var(--forest-3) 100%);
  }
  .hero-title {
    position: absolute; top: 90px; left: 0; width: 100%; text-align: center;
    font-family: "Lato", Arial, sans-serif; font-weight: 900;
    font-size: 46px; color: var(--white); letter-spacing: 0.2px;
  }
  .hero-subtitle {
    position: absolute; top: 155px; left: 0; width: 100%; text-align: center;
    font-family: "Lato", Arial, sans-serif; font-weight: 700;
    font-size: 25px; color: var(--white);
  }

  /* Search */
  .search-bar {
    position: absolute; left: 189px; top: 233px; width: 821px; height: 77px;
    background: var(--bar-shade); border-radius: 3px;
  }
  .search-group {
    position: absolute; top: 7px; height: 64px;
    background: var(--white); border-radius: 3px; display: flex;
  }
  .search-group--what { left: 7px; width: 384px; }
  .search-group--when { left: 398px; width: 226px; }
  .search-field {
    height: 100%; display: flex; flex-direction: column; justify-content: center;
    align-items: center; font-size: 16px; color: var(--ink-soft);
    border-right: 1px solid var(--divider);
    margin: 4px 0;
    height: auto;
  }
  .search-field:last-child { border-right: none; }
  .search-field--species { width: 136px; align-items: flex-start; padding-left: 17px; }
  .search-field--country { width: 128px; }
  .search-field--offers { width: 120px; }
  .search-field--checkin { width: 111px; }
  .search-field--checkout { width: 115px; }
  .species-group { font-weight: 700; font-size: 17px; color: var(--ink); line-height: 1.2; }
  .species-name { font-size: 14px; color: var(--ink-soft); line-height: 1.3; }
  .search-button {
    position: absolute; left: 631px; top: 7px; width: 183px; height: 64px;
    background: var(--orange); border: none; border-radius: 3px;
    display: flex; align-items: center; justify-content: center; gap: 9px;
    color: var(--white); font-family: "Open Sans", Arial, sans-serif;
    font-weight: 700; font-size: 16px; letter-spacing: 0.3px;
  }
</style>
</head>
<body>
<div class="page">
  <header class="site-header">
    <a class="brand" href="#">
      <span class="brand-mark"></span>
      <span class="brand-name">ferntrail.online</span>
    </a>
    <nav class="main-nav">
      <a href="#">Countries</a>
      <a href="#">Wild species</a>
      <a href="#">About us</a>
      <a href="#">Terms and conditions</a>
      <a href="#">How it works</a>
      <a class="partner-button" href="#">Become A Partner</a>
    </nav>
  </header>

  <section class="hero">
    <div class="hero-photo" role="img" aria-label="Misty pine forest with tall dark conifers fading into fog"></div>
    <h1 class="hero-title">You don't need a hunting organizer!</h1>
    <p class="hero-subtitle">Book directly at the ferntrail.online</p>

    <form class="search-bar">
      <div class="search-group search-group--what">
        <div class="search-field search-field--species">
          <span class="species-group">Cervids</span>
          <span class="species-name">Red deer bull</span>
        </div>
        <div class="search-field search-field--country">Country</div>
        <div class="search-field search-field--offers">Offers</div>
      </div>
      <div class="search-group search-group--when">
        <div class="search-field search-field--checkin">Check In</div>
        <div class="search-field search-field--checkout">Check Out</div>
      </div>
      <button class="search-button" type="button">
        <svg width="17" height="17" viewBox="0 0 17 17" aria-hidden="true">
          <circle cx="10" cy="7" r="5" fill="none" stroke="#ffffff" stroke-width="2.4"/>
          <line x1="6.3" y1="10.7" x2="1.8" y2="15.2" stroke="#ffffff" stroke-width="2.8" stroke-linecap="round"/>
        </svg>
        SEARCH
      </button>
    </form>
  </section>
</div>
</body>
</html>
```